依頼詳細
おしゃれなイメージを希望しています。

掲載してもらいたい内容を載せています
宜しくお願いします。
①24時間営業
②11/6新規オープン(予定です。後日決定します)
③アクセスマップ(新しくできた『ふわりGATE』というモール内にコインランドリーが開店するということがわかるように)国道217号沿いでハナマルマートがあります。
④店内写真、屋外写真
⑤12/14まで全機種半額
洗濯乾燥8kg 900円→400円
洗濯乾燥15kg 1200円→600円
洗濯乾燥22kg 1500円→700円
洗濯のみ15kg 600円→300円
洗濯のみ22kg 900円→400円
洗濯のみ32kg 1100円→500円
乾燥のみ14kg 100円/10分→100円/20分
乾燥のみ25kg 100円/8分→100円/16分
シューズ用洗濯機 200円→100円
⑤洗濯機から乾燥機に移す面倒な手間いらずの全自動洗濯乾燥機を導入
⑥ふとんクリーニング店プロデュースなので羽毛布団、こたつ布団、毛布の洗濯も安心
⑦天然由来成分とEM(人体にも環境にもやさしい善玉菌の集合体)を配合した洗剤を使用しています。
記載項目
店名ロゴ(添付)、住所(大分市北松原215-3ふわりGATE C-204)、地図、店舗写真、店内写真
サイズ
A5
ページ数
両面
希望イメージ
シンプル 複雑
単色 カラフル
暗い 明るい
日常 高級
遊び心 厳粛
未来的 伝統的
女性的 男性的
希望する色
設定なし
納品ファイル
• イラストレーター形式 (.ai)
補足説明
店舗写真、店内写真は添付写真を当て込んでください。正式な写真は後日差し替えをお願いします。
新規のモール内の店舗ですので地図は大きめに表記をお願いします。
納品はアウトライン化したものとしていないものの両方お願いします。イラストレーターCS2で開けるようにしてください

訴求したい内容が一目でわかりやすい提案だったから

このたびはお忙しい中、多数のご提案をいただきありがとうございました。
今後も依頼していきますので機会がありましたらご提案くださいますようお願いします。
今後ともよろしくお願いします。

```html
<!DOCTYPE html>
<html lang="ja">
<head>
<meta charset="utf-8">
<title>Honwaka Laundry グランドオープン</title>
<link href="https://fonts.googleapis.com/css2?family=Oswald:wght@600;700&family=Zen+Maru+Gothic:wght@700;900&display=swap" rel="stylesheet">
<style>
  :root{
    --sky:#a6d3d9;
    --navy:#26313d;
    --white:#ffffff;
    --accent:#e2445c;
    --yellow:#f6e04b;
    --photo-a:#d9d4cb;
    --photo-b:#9b8b76;
  }
  *{margin:0;padding:0;box-sizing:border-box}
  html,body{width:849px;height:1200px;overflow:hidden;background:var(--sky)}
  .flyer{position:relative;width:849px;height:1200px;background:var(--sky);
    font-family:"Zen Maru Gothic",sans-serif;color:var(--navy)}
  .frame{position:absolute;inset:18px;border:3px solid var(--white);border-radius:22px}
  .badge-24h{position:absolute;left:30px;top:32px;width:140px;height:140px;border-radius:50%;
    background:var(--navy);color:var(--white);display:flex;flex-direction:column;
    align-items:center;justify-content:center;font-weight:900;line-height:1}
  .badge-24h .num{font-size:46px;font-family:"Oswald",sans-serif}
  .badge-24h .txt{font-size:34px;margin-top:4px}
  .brand{position:absolute;left:0;right:0;top:44px;text-align:center;font-weight:900}
  .brand .kana{font-size:13px;letter-spacing:2px}
  .brand .name{font-size:30px;letter-spacing:1px}
  .badge-deal{position:absolute;right:46px;top:44px;width:104px;height:104px;border-radius:50%;
    background:var(--white);color:var(--accent);font-size:13px;font-weight:900;
    display:flex;align-items:center;justify-content:center;text-align:center;line-height:1.35}
  .headline{position:absolute;left:0;right:0;text-align:center;font-family:"Oswald",sans-serif;
    font-weight:700;color:var(--navy);line-height:1}
  .headline.grand{top:120px;font-size:104px;letter-spacing:2px}
  .headline.open{top:222px;font-size:180px;letter-spacing:2px}
  .icon{position:absolute}
  .icon.car{left:96px;top:258px}
  .icon.washer{right:92px;top:246px}
  .intro{position:absolute;left:0;right:0;top:412px;text-align:center;font-weight:900;font-size:22px;line-height:1.5}
  .intro .hl{color:var(--accent)}
  .photo-store{position:absolute;left:44px;top:490px;width:761px;height:330px;
    background:linear-gradient(180deg,var(--photo-a),var(--photo-b))}
  .photo-staff{position:absolute;right:44px;top:640px;width:300px;height:480px;
    background:linear-gradient(180deg,#8a7866,#4e4138);border-radius:6px}
  .bubble-night{position:absolute;left:64px;top:510px;padding:12px 20px;background:var(--navy);
    color:var(--white);font-size:19px;font-weight:900;border-radius:28px}
  .bubble-gosh{position:absolute;right:40px;top:740px;width:96px;height:96px;border-radius:50%;
    background:var(--yellow);color:var(--navy);font-family:"Oswald",sans-serif;font-weight:700;
    font-size:19px;line-height:1.05;display:flex;align-items:center;justify-content:center;text-align:center}
  .date-open,.date-sale{position:absolute;left:48px;display:flex;align-items:flex-end;
    font-family:"Oswald",sans-serif;font-weight:700;color:var(--navy);line-height:.9}
  .date-open{top:880px}
  .date-sale{top:1000px}
  .md{display:flex;flex-direction:column;align-items:flex-end;font-size:44px;margin-right:4px}
  .md small{font-size:22px;font-family:"Zen Maru Gothic",sans-serif;font-weight:900}
  .big{font-size:110px}
  .arrow{font-size:64px;margin:0 6px 12px}
  .open-word{font-size:92px}
  .until{font-family:"Zen Maru Gothic",sans-serif;font-size:26px;font-weight:900;line-height:1.1;margin:0 10px 16px}
  .half{font-family:"Zen Maru Gothic",sans-serif;font-size:84px;font-weight:900;
    background:linear-gradient(transparent 55%,var(--yellow) 55%);padding:0 4px}
</style>
</head>
<body>
<div class="flyer">
  <div class="frame"></div>

  <div class="badge-24h"><span class="num">24時間</span><span class="txt">営業</span></div>

  <div class="brand">
    <div class="kana">ほんわかランドリー</div>
    <div class="name">Honwaka Laundry</div>
  </div>

  <div class="badge-deal">オープン記念<br>期間限定<br>全機種半額</div>

  <svg class="icon car" width="78" height="40" viewBox="0 0 78 40" aria-hidden="true">
    <path d="M4 30 V20 L16 18 L26 6 H52 L64 18 L74 20 V30 Z" fill="var(--navy)"/>
    <rect x="30" y="10" width="10" height="8" fill="var(--sky)"/>
    <rect x="44" y="10" width="10" height="8" fill="var(--sky)"/>
    <circle cx="20" cy="31" r="7" fill="var(--navy)" stroke="var(--sky)" stroke-width="3"/>
    <circle cx="58" cy="31" r="7" fill="var(--navy)" stroke="var(--sky)" stroke-width="3"/>
  </svg>
  <svg class="icon washer" width="48" height="58" viewBox="0 0 48 58" aria-hidden="true">
    <rect x="2" y="2" width="44" height="54" rx="5" fill="none" stroke="var(--navy)" stroke-width="4"/>
    <line x1="2" y1="14" x2="46" y2="14" stroke="var(--navy)" stroke-width="3"/>
    <circle cx="24" cy="35" r="12" fill="none" stroke="var(--navy)" stroke-width="4"/>
  </svg>

  <div class="headline grand">GRAND</div>
  <div class="headline open">OPEN!</div>

  <p class="intro">大分市北松原215-3 ふわりGATE C-204に<br><span class="hl">24時間営業</span>のコインランドリーが誕生がオープン!</p>

  <div class="photo-store" role="img" aria-label="店内写真：並んだ洗濯機と乾燥機、木目の床"></div>
  <div class="bubble-night">夜が遅いパパにも<br>行ってもらえる♪</div>
  <div class="photo-staff" role="img" aria-label="洗濯かごを持つエプロン姿の男性スタッフの写真"></div>
  <div class="bubble-gosh">Oh,my..<br>GOSH!!</div>

  <div class="date-open">
    <span class="md">11/<small>Tue</small></span>
    <span class="big">6</span>
    <span class="arrow">→</span>
    <span class="open-word">OPEN!</span>
  </div>
  <div class="date-sale">
    <span class="md">12/<small>Fri</small></span>
    <span class="big">14</span>
    <span class="until">まで<br>全機種</span>
    <span class="half">半額</span>
  </div>
</div>
</body>
</html>
```